Rising Paths Web Design

I am starting a new company that will provide LIFE COACHING services - I have tried to design a website, but it's too complicated. Right now, it's just me - I'm the only person that will provide services through the website - I have used artmarket to purchase a logo (see below). I want to be able to update the website myself, but need a template - basic design. Because I am not technologically savvy enough to explain in words - I basically want to have a website that will provide basic information about my services (coaching), a page about me and my background, hopefully scheduling possibilities, and testimonials — also a page for writing/blogs. I bought a website through NetHarbor - so when I have a template, I guess I”d use that - but maybe I’ll need to work with a designer to actually get it up on the internet. I have a head shot that I’ll upload, too.
Target Market(s)
Clients from the independent (private school) world - teachers, administrators
Number of Pages Required
4 page
Look and feel
Each slider illustrates characteristics of the customer's brand and the style your logo design should communicate.

```html
<!DOCTYPE html>
<html lang="en">
<head>
<meta charset="utf-8">
<title>Rising Paths – Life Coaching</title>
<link href="https://fonts.googleapis.com/css2?family=EB+Garamond:wght@400;500&family=Montserrat:wght@400;500;600;700&display=swap" rel="stylesheet">
<style>
:root{
  --teal:#0aaa89;
  --teal-dark:#07957a;
  --mint:#e8f8f4;
  --ink:#2f3437;
  --muted:#6b7073;
  --line:#e7ecea;
  --stage:#f4f4f4;
  --white:#ffffff;
  --sun:#f7c400;
  --cream:#f6fbd6;
  --charcoal:#3a3d3f;
}
*{box-sizing:border-box;margin:0;padding:0}
html,body{width:1200px;height:1200px;overflow:hidden;background:var(--stage)}
.stage{width:1932px;height:1932px;transform:scale(.62112);transform-origin:0 0;position:relative;background:var(--stage)}
.page{position:absolute;left:702px;top:57px;width:528px;height:1818px;background:var(--white);font-family:"Montserrat",sans-serif;color:var(--ink);box-shadow:0 0 30px rgba(0,0,0,.05)}
.abs{position:absolute}
.serif{font-family:"EB Garamond",serif;font-weight:400}
.btn{position:absolute;background:var(--teal);color:#fff;font-size:5px;border-radius:2px;display:flex;align-items:center;justify-content:center}
.btn.dark{background:var(--charcoal)}
.small{font-size:5.2px;line-height:8.4px;color:var(--muted)}
/* nav */
.nav a{position:absolute;top:23px;font-size:5px;color:var(--ink);text-decoration:none}
.nav .active{border-bottom:1px solid var(--teal);padding-bottom:3px}
.brand{position:absolute;display:flex;flex-direction:column;align-items:center;font-family:"EB Garamond",serif;font-size:5px;color:var(--ink)}
.brand .mark{width:28px;height:28px;border:1px solid var(--teal);border-radius:50%;display:flex;align-items:center;justify-content:center}
/* hero */
.hero{position:absolute;left:0;top:51px;width:528px;height:247px;background:var(--teal);overflow:hidden}
.hero .frame{position:absolute;left:55px;top:20px;width:126px;height:192px;border:1px solid rgba(255,255,255,.6);border-radius:60px 60px 4px 4px}
.hero .photo{position:absolute;left:61px;top:39px;width:109px;height:168px;border-radius:52px 52px 3px 3px;background:linear-gradient(160deg,#cfc6b2,#e9dfcf 55%,#b7ad9d)}
.badge{position:absolute;background:#fff}
.hero h1{position:absolute;left:232px;top:61px;font-size:27px;line-height:30px;color:#fff}
.hero .tag{position:absolute;left:232px;top:50px;font-size:4.2px;color:#fff}
.hero p{position:absolute;left:232px;width:190px;font-size:5px;line-height:8.4px;color:#eafaf5}
/* cards */
.card{position:absolute;background:#fff;border:1px solid var(--line);border-radius:6px}
.card h4{font-size:6.2px;font-weight:600;margin-bottom:6px}
.h2{position:absolute;font-family:"EB Garamond",serif;font-size:18px;line-height:20px;color:var(--ink)}
.leaf{position:absolute}
.quote{font-size:5.2px;line-height:9px;color:var(--muted);text-align:center}
.avatar{width:38px;height:38px;border-radius:50%;margin:14px auto 10px;background:linear-gradient(160deg,#8a6a52,#d6c3b0)}
.stars{color:var(--sun);font-size:8px;letter-spacing:2px;text-align:center}
.blog .img{height:78px;border-radius:6px 6px 0 0}
.blog .body{padding:14px 13px}
.blog h5{font-size:5.2px;font-weight:600;margin-bottom:2px}
.footer-links a{font-size:4.6px;color:var(--muted);margin:0 8px;text-decoration:none}
</style>
</head>
<body>
<div class="stage">
<div class="page">

  <!-- navigation -->
  <nav class="nav">
    <a class="active" style="left:57px">Home</a>
    <a style="left:90px">Services</a>
    <a style="left:129px">About me</a>
  </nav>
  <div class="brand" style="left:240px;top:10px;width:48px">
    <div class="mark"><span>Rising Paths</span></div>
  </div>
  <div class="btn" style="left:422px;top:19px;width:52px;height:13px">Let's Talk</div>

  <!-- hero -->
  <section class="hero">
    <div class="frame"></div>
    <div class="photo" role="img" aria-label="Head shot of the coach, smiling, in a light scarf"></div>
    <div class="badge" style="left:154px;top:25px;width:24px;height:18px;border-radius:2px"></div>
    <div class="badge" style="left:50px;top:112px;width:22px;height:22px;border-radius:50%;border:2px solid #5fb7e0"></div>
    <div class="badge" style="left:163px;top:178px;width:26px;height:26px;border-radius:3px;background:#264d73"></div>
    <div class="tag">Proven strategies backed by science for success.</div>
    <h1 class="serif">Live life at<br>the full potential</h1>
    <p style="top:136px">Lorem ipsum dolor sit amet, consectetur adipiscing elit, sed do eiusmod tempor incididunt ut labore et dolore magna aliqua minim veniam.</p>
    <p style="top:170px">Sed ut perspiciatis unde omnis iste natus error sit voluptatem accusantium doloremque laudantium.</p>
  </section>

  <!-- services -->
  <svg class="leaf" style="left:54px;top:335px" width="32" height="24" viewBox="0 0 32 24" role="img" aria-label="Leaf sprig ornament"><path d="M2 22 Q14 12 30 4" stroke="#9fdccb" fill="none" stroke-width=".8"/></svg>
  <h2 class="h2" style="left:54px;top:362px">I can help you in these<br>particular areas.</h2>
  <p class="small abs" style="left:238px;top:362px;width:236px">Lorem ipsum dolor sit amet, consectetur adipiscing elit, sed do eiusmod tempor incididunt ut labore et dolore magna aliqua minim veniam.</p>
  <p class="small abs" style="left:238px;top:388px;width:236px">Sed ut perspiciatis unde omnis iste natus error sit voluptatem accusantium doloremque laudantium, totam rem aperiam, eaque ipsa quae ab illo inventore veritatis et quasi architecto beatae vitae dicta sunt explicabo.</p>

  <div class="card" style="left:54px;top:430px;width:135px;height:132px;padding:26px 17px">
    <svg width="30" height="16" viewBox="0 0 30 16"><circle cx="8" cy="9" r="5" fill="none" stroke="#2f3437" stroke-width=".8"/><circle cx="22" cy="9" r="5" fill="none" stroke="#2f3437" stroke-width=".8"/></svg>
    <h4 style="margin-top:6px">1:1 Coaching</h4>
    <p class="small">Lorem ipsum dolor sit amet, consectetur adipiscing elit, sed do eiusmod tempor incididunt ut labore et dolore magna aliqua minim veniam.</p>
  </div>
  <div class="card" style="left:196px;top:430px;width:135px;height:132px;padding:26px 17px">
    <svg width="30" height="16" viewBox="0 0 30 16"><rect x="3" y="1" width="14" height="4" fill="none" stroke="#2f3437" stroke-width=".8"/><circle cx="6" cy="9" r="2" fill="none" stroke="#2f3437" stroke-width=".8"/><circle cx="14" cy="9" r="2" fill="none" stroke="#2f3437" stroke-width=".8"/><path d="M2 15 Q6 11 10 15 M10 15 Q14 11 18 15" fill="none" stroke="#2f3437" stroke-width=".8"/></svg>
    <h4 style="margin-top:6px">Consultation</h4>
    <p class="small">Lorem ipsum dolor sit amet, consectetur adipiscing elit, sed do eiusmod tempor incididunt ut labore et dolore magna aliqua minim veniam.</p>
  </div>
  <div class="card" style="left:338px;top:430px;width:136px;height:132px;padding:26px 17px">
    <svg width="30" height="16" viewBox="0 0 30 16"><rect x="10" y="1" width="8" height="5" fill="none" stroke="#0aaa89" stroke-width=".8"/><g fill="none" stroke="#2f3437" stroke-width=".8"><circle cx="4" cy="8" r="2"/><circle cx="10" cy="10" r="2"/><circle cx="16" cy="10" r="2"/><path d="M1 15h18"/></g></svg>
    <h4 style="margin-top:6px">Group Coaching Sessions</h4>
    <p class="small">Lorem ipsum dolor sit amet, consectetur adipiscing elit, sed do eiusmod tempor incididunt ut labore et dolore magna aliqua minim veniam.</p>
  </div>
  <div class="btn" style="left:238px;top:578px;width:52px;height:15px">All Services</div>

  <!-- testimonials -->
  <section class="abs" style="left:0;top:624px;width:528px;height:326px;background:var(--mint)">
    <h2 class="h2" style="left:54px;top:64px">Hear out what my<br>clients say about me.</h2>
    <div class="card" style="left:54px;top:117px;width:135px;height:153px;padding:16px 18px">
      <p class="quote">“Thank you so much for this online training. The training was very clear and well organized with beautiful examples and videos.”</p>
      <div class="avatar" role="img" aria-label="Client portrait"></div>
      <p style="font-size:5.5px;text-align:center;margin-bottom:3px">Ava</p><p class="stars">★★★★★</p>
    </div>
    <div class="card" style="left:196px;top:117px;width:135px;height:153px;padding:16px 18px">
      <p class="quote">“Thank you so much for this online training. The training was very clear and well organized with beautiful examples and videos.”</p>
      <div class="avatar" role="img" aria-label="Client portrait"></div>
      <p style="font-size:5.5px;text-align:center;margin-bottom:3px">Lana</p><p class="stars">★★★★★</p>
    </div>
    <div class="card" style="left:338px;top:117px;width:136px;height:153px;padding:16px 18px">
      <p class="quote">“Thank you so much for this online training. The training was very clear and well organized with beautiful examples and videos.”</p>
      <div class="avatar" role="img" aria-label="Client portrait"></div>
      <p style="font-size:5.5px;text-align:center;margin-bottom:3px">Ava</p><p class="stars">★★★★★</p>
    </div>
  </section>

  <!-- blog -->
  <h2 class="h2" style="left:0;width:528px;top:1007px;text-align:center">Stay Motivated, read<br>the weekly blog articles.</h2>
  <div class="card blog" style="left:54px;top:1058px;width:135px;height:167px">
    <div class="img" role="img" aria-label="Two women talking at a laptop in a brick-walled office" style="background:linear-gradient(135deg,#b9774e,#3d8fb0 60%,#2b2b2b)"></div>
    <div class="body"><h5>Balancing your love and work life.</h5><p class="small">Lorem ipsum dolor sit amet, consectetur adipiscing elit, sed do eiusmod tempor incididunt ut labore et dolore magna aliqua minim veniam.</p></div>
  </div>
  <div class="card blog" style="left:196px;top:1058px;width:135px;height:167px">
    <div class="img" role="img" aria-label="Person sitting outdoors using a phone" style="background:linear-gradient(135deg,#5d7d3a,#2a2f36 55%,#1c1f24)"></div>
    <div class="body"><h5>Balancing your love and work life.</h5><p class="small">Lorem ipsum dolor sit amet, consectetur adipiscing elit, sed do eiusmod tempor incididunt ut labore et dolore magna aliqua minim veniam.</p></div>
  </div>
  <div class="card blog" style="left:338px;top:1058px;width:136px;height:167px">
    <div class="img" role="img" aria-label="Woman sitting on a mountain ridge at sunset" style="background:linear-gradient(180deg,#e7c7a8,#b07c66 60%,#6e4d45)"></div>
    <div class="body"><h5>Balancing your love and work life.</h5><p class="small">Lorem ipsum dolor sit amet, consectetur adipiscing elit, sed do eiusmod tempor incididunt ut labore et dolore magna aliqua minim veniam.</p></div>
  </div>
  <div class="btn" style="left:228px;top:1244px;width:72px;height:15px">Read more blogs</div>

  <!-- free guide -->
  <section class="abs" style="left:0;top:1291px;width:528px;height:262px;background:var(--teal)">
    <h2 class="h2" style="left:54px;top:66px;color:#fff">Don’t miss out on my<br>‘Live life at the full potential’<br>free guide</h2>
    <p class="small abs" style="left:54px;top:139px;width:212px;color:#e6f8f2">Lorem ipsum dolor sit amet, consectetur adipiscing elit, sed do eiusmod tempor incididunt ut labore et dolore magna aliqua minim veniam.</p>
    <p class="small abs" style="left:54px;top:165px;width:212px;color:#e6f8f2">Sed ut perspiciatis unde omnis iste natus error sit voluptatem accusantium doloremque laudantium, totam rem aperiam, eaque ipsa quae ab illo inventore veritatis et quasi architecto beatae vitae dicta sunt explicabo.</p>
    <div class="btn dark" style="left:54px;top:205px;width:96px;height:15px">Read your free guide now</div>
    <div class="abs" style="left:340px;top:35px;width:137px;height:185px;background:var(--cream)">
      <p class="abs" style="left:16px;top:22px;font-size:12px;font-weight:700;line-height:16px;color:var(--ink)">Are you<br>Ready to<br>Transform<br>Your life?</p>
      <div class="abs" role="img" aria-label="Head shot of the coach" style="left:54px;top:70px;width:83px;height:115px;border-radius:60px 0 0 0;background:linear-gradient(160deg,#cfc6b2,#e9dfcf 55%,#b7ad9d)"></div>
    </div>
    <div class="abs" style="left:453px;top:31px;width:36px;height:36px;border-radius:50%;background:var(--sun);color:#fff;font-size:5px;display:flex;align-items:center;justify-content:center;text-align:center;line-height:8px">Free<br>Guide</div>
  </section>

  <!-- newsletter -->
  <div class="abs" style="left:53px;top:1585px;width:422px;height:64px;background:var(--mint);border-radius:6px">
    <p class="serif abs" style="left:18px;top:16px;font-size:10px">Get notified when I publish new articles</p>
    <p class="small abs" style="left:18px;top:31px;width:120px">Stay up to date with the latest news, announcements, and articles.</p>
    <div class="abs" style="left:205px;top:28px;width:148px;height:14px;background:#fff;border:1px solid var(--line);font-size:4.6px;color:#bbb;padding:4px 6px">Enter your email</div>
    <div class="btn dark" style="left:353px;top:28px;width:55px;height:14px">Subscribe</div>
  </div>

  <!-- footer -->
  <div class="brand" style="left:240px;top:1668px;width:48px">
    <div class="mark"><span>Rising Paths</span></div>
  </div>
  <p class="abs" style="left:146px;top:1709px;width:236px;text-align:center;font-size:4.6px;line-height:8px;color:var(--muted)">Lorem ipsum dolor sit amet, consectetur adipiscing elit, sed do eiusmod tempor incididunt ut labore et dolore magna aliqua minim veniam. Sed ut perspiciatis unde omnis iste natus error sit voluptatem accusantium doloremque laudantium, totam rem aperiam, eaque ipsa quae ab illo inventore veritatis et quasi architecto beatae vitae dicta sunt explicabo.</p>
  <div class="abs" style="left:248px;top:1748px;display:flex;gap:4px">
    <span style="width:8px;height:8px;border-radius:50%;background:var(--mint)"></span>
    <span style="width:8px;height:8px;border-radius:50%;background:var(--mint)"></span>
    <span style="width:8px;height:8px;border-radius:50%;background:var(--mint)"></span>
  </div>
  <div class="abs" style="left:53px;top:1768px;width:422px;height:1px;background:var(--line)"></div>
  <div class="abs footer-links" style="left:0;top:1782px;width:528px;text-align:center">
    <a>Home</a><a>Services</a><a>About me</a><a>Blog</a><a>Contact</a>
  </div>
  <p class="abs" style="left:0;top:1797px;width:528px;text-align:center;font-size:4.2px;color:#aaa">© 2022 rising paths</p>

</div>
</div>
</body>
</html>
```